Need an event poster for an automotive event.
The event is a half mile trap speed event. Sometimes called a MaxPace event, they have a 1/2 mile to see how fast They can go. They run one car at a time, it is not a side-by-side race.
Title of the event is “RVLO Sidevalve Autumn Classic”. Dates are October 3-4 2020. Location Blytheville Arkansas. Website is RVLOstretch.com. Most participants will be 50 and older .
All entries must be a carbureted flathead engine .

```html
<!DOCTYPE html>
<html lang="en">
<head>
<meta charset="utf-8">
<title>RVLO Sidevalve Autumn Classic</title>
<link rel="stylesheet" href="https://fonts.googleapis.com/css2?family=Bebas+Neue&display=swap">
<style>
  :root {
    --ink: #ffffff;
    --night: #000000;
    --deep-red: #3a0000;
    --red: #d10a0a;
    --glow: #ff2a1a;
  }
  * { margin: 0; padding: 0; box-sizing: border-box; }
  html, body { width: 849px; height: 1200px; overflow: hidden; background: var(--night); }
  .poster {
    position: relative;
    width: 849px;
    height: 1200px;
    overflow: hidden;
    background: linear-gradient(180deg, #150404 0%, #0a0202 60%, var(--night) 100%);
    font-family: "Bebas Neue", "Arial Narrow", sans-serif;
    color: var(--ink);
  }
  .hero-art {
    position: absolute;
    left: 0; top: 0;
    width: 849px; height: 800px;
    background:
      radial-gradient(circle at 50% 52%, #0a0000 0 70px, transparent 72px),
      radial-gradient(circle at 50% 52%, #5a0000 0 160px, var(--red) 250px, #8a0202 330px, transparent 345px),
      radial-gradient(ellipse at 55% 50%, rgba(255,42,26,.55) 0%, rgba(90,0,0,.6) 45%, transparent 75%),
      linear-gradient(180deg, #2a2a2a 0%, #3a0a0a 25%, #7a0606 50%, #2a0202 85%, #0a0202 100%);
  }
  .club-name {
    position: absolute;
    left: 84px; top: 392px;
    width: 690px;
    text-align: center;
    font-size: 330px;
    line-height: 1;
    letter-spacing: 6px;
    color: var(--ink);
  }
  .details {
    position: absolute;
    left: 101px;
    width: 648px;
    display: flex;
    align-items: center;
    justify-content: space-between;
    white-space: nowrap;
    font-weight: 400;
    line-height: 1;
  }
  .event-title { top: 808px; font-size: 72px; letter-spacing: 1px; }
  .event-format { top: 902px; gap: 24px; font-size: 54px; }
  .event-format .rule { flex: 1; height: 2px; background: var(--ink); }
  .event-format .label { letter-spacing: 1px; }
  .event-perks { top: 968px; font-size: 40px; }
  .divider { position: absolute; left: 101px; top: 1030px; width: 648px; height: 2px; background: var(--ink); }
  .event-info { top: 1050px; font-size: 28px; letter-spacing: 1.5px; }
</style>
</head>
<body>
  <main class="poster">
    <div class="hero-art" role="img" aria-label="Glowing red speedometer dial over a waving black and white checkered flag"></div>
    <div class="club-name">RVLO</div>

    <h1 class="details event-title"><span>Sidevalve</span><span>Autumn</span><span>Classic</span></h1>
    <p class="details event-format">
      <span class="rule"></span>
      <span class="label">1/2 Mile Speed Trials</span>
      <span class="rule"></span>
    </p>
    <p class="details event-perks"><span>Trophies Awards</span><span>|</span><span>Certified Speed Certificates</span></p>
    <div class="divider"></div>
    <p class="details event-info"><span>October 3-4 2020</span><span>|</span><span>Blytheville Arkansas</span><span>|</span><span>RVLOstretch.com</span></p>
  </main>
</body>
</html>
```